KVT Business Cards

We require business cards for our business. We would like a matte black back to the card, with our logo centred in the middle. The front side of the card is open to design.

Target Market(s)

Clients looking for legal services (professional)

Industry/Entity Type

Legal

Contact Information for Business Card

Boris Telemark
Partner
Mobile: 0438 715 642
Email: boris@kvtlaw.co
Website: www.kvtlaw.co
Level 3, 118 Wexbury Street
Sydney NSW 2000

Font styles to use
Other font styles liked:
• Avenir

Colors
f04a50
ffffff
1b1b1b

Requirements
Must have
• Black back with logo included in the centre of the card.
• Our font is Avenir.

```html
<!DOCTYPE html>
<html lang="en">
<head>
<meta charset="utf-8">
<title>KVT Business Cards</title>
<link href="https://fonts.googleapis.com/css2?family=Nunito+Sans:wght@400;600;700;800&display=swap" rel="stylesheet">
<style>
  :root{
    --red:#c8183f;
    --accent:#f04a50;
    --ink:#1b1b1b;
    --paper:#ffffff;
    --stage:#2b2b2e;
    --back:#080808;
    --ghost-dark:rgba(255,255,255,0.07);
    --ghost-light:#e3e3e3;
    --rule:#1b1b1b;
  }
  *{box-sizing:border-box;margin:0;padding:0}
  html,body{width:1200px;height:800px;overflow:hidden;background:var(--stage)}
  body{font-family:"Nunito Sans",Arial,sans-serif;position:relative}

  .card{position:absolute;width:540px;height:310px;border-radius:26px;overflow:hidden}

  /* Back side */
  .card-back{left:60px;top:90px;background:var(--back)}
  .card-back .ghost{position:absolute;right:34px;top:18px;font-size:120px;font-weight:800;letter-spacing:6px;color:var(--ghost-dark);line-height:1}
  .brand{position:absolute;display:flex;align-items:center;gap:16px}
  .card-back .brand{left:50%;top:50%;transform:translate(-50%,-50%)}
  .brand-mark{width:34px;height:34px;background:var(--red);flex:none}
  .brand-name{font-weight:700;font-size:24px;line-height:1.02;text-transform:uppercase;letter-spacing:.5px}
  .card-back .brand-name{color:var(--paper)}

  /* Front side */
  .card-front{left:600px;top:400px;background:var(--paper)}
  .card-front .ghost{position:absolute;right:30px;top:14px;font-size:110px;font-weight:800;letter-spacing:6px;color:var(--ghost-light);line-height:1}
  .card-front .brand{left:40px;top:92px}
  .card-front .brand-name{color:var(--ink);font-size:22px}
  .divider{position:absolute;left:40px;right:40px;top:172px;height:1px;background:var(--rule)}
  .divider::after{content:"";position:absolute;right:0;top:0;width:34%;height:1px;background:var(--red)}
  .address{position:absolute;right:40px;top:182px;text-align:right;font-size:11px;color:var(--ink);line-height:1.45}
  .person{position:absolute;left:40px;top:184px}
  .person-name{color:var(--red);font-weight:800;font-size:17px;text-transform:uppercase;letter-spacing:.3px;line-height:1.1}
  .person-role{font-size:12px;text-transform:uppercase;color:var(--ink);letter-spacing:.5px;margin-bottom:8px}
  .contact{list-style:none}
  .contact li{display:flex;align-items:center;gap:8px;font-size:11px;color:var(--ink);margin-bottom:3px}
  .contact svg{width:15px;height:15px;flex:none}
  .edge-band{position:absolute;left:0;right:0;bottom:0;height:14px;background:var(--red)}
</style>
</head>
<body>

<section class="card card-back" aria-label="Card back">
  <div class="ghost" aria-hidden="true">KVT</div>
  <div class="brand">
    <span class="brand-mark"></span>
    <div class="brand-name">Karlsson<br>Vidakovic<br>Legal</div>
  </div>
</section>

<section class="card card-front" aria-label="Card front">
  <div class="ghost" aria-hidden="true">KVT</div>
  <div class="brand">
    <span class="brand-mark"></span>
    <div class="brand-name">Karlsson<br>Vidakovic<br>Legal</div>
  </div>

  <div class="divider"></div>

  <address class="address" style="font-style:normal">
    Level 3, 118 Wexbury Street<br>
    Sydney NSW 2000
  </address>

  <div class="person">
    <div class="person-name">Boris Telemark</div>
    <div class="person-role">Partner</div>
    <ul class="contact">
      <li>
        <svg viewBox="0 0 16 16"><rect width="16" height="16" fill="#c8183f"/><rect x="5" y="3" width="6" height="10" rx="1" fill="none" stroke="#fff" stroke-width="1.2"/><circle cx="8" cy="11" r=".7" fill="#fff"/></svg>
        0438 715 642
      </li>
      <li>
        <svg viewBox="0 0 16 16"><rect width="16" height="16" fill="#c8183f"/><rect x="3" y="4.5" width="10" height="7" fill="none" stroke="#fff" stroke-width="1.2"/><path d="M3 4.5l5 4 5-4" fill="none" stroke="#fff" stroke-width="1.2"/></svg>
        boris@kvtlaw.co
      </li>
      <li>
        <svg viewBox="0 0 16 16"><rect width="16" height="16" fill="#c8183f"/><circle cx="8" cy="8" r="4.5" fill="none" stroke="#fff" stroke-width="1.1"/><path d="M3.5 8h9M8 3.5c-2 2.5-2 6.5 0 9M8 3.5c2 2.5 2 6.5 0 9" fill="none" stroke="#fff" stroke-width=".9"/></svg>
        www.kvtlaw.co
      </li>
    </ul>
  </div>

  <div class="edge-band"></div>
</section>

</body>
</html>
```